Legal Services Power Point

Need a PP template for a legal consulting company - we prefer the use of our logo colors. Also- emphasis on international/global business with images of the USA because we serve immigration and international business coming to the US and we will use the PP to make presentations in other countries. The Company is Brackwell Law Firm PC ( logo uploaded) but we have do business outside the US as Brackwell Consulting Group ( logo upoaded too)

Target Market(s)

Business clients

Industry/Entity Type

Legal/ International Cross-Border/ Immigration

Font styles to use
Sans Serif

Colors
0054AA
0677BA
7BADD7
CADEEF
E8F1F8

Requirements
Must have
• International elements, global, US, we do immigration and legal consulting for foreign business
Nice to have
• Make it look elegant as we are in the legal and consulting business.

```html
<!DOCTYPE html>
<html lang="en">
<head>
<meta charset="utf-8">
<title>Brackwell Law Firm PC – Presentation Template</title>
<link rel="stylesheet" href="https://fonts.googleapis.com/css2?family=Montserrat:wght@400;500;600;700;800&display=swap">
<style>
:root{
  --navy:#2d2c73;
  --navy-deep:#1f1e5a;
  --red:#c3203a;
  --ink:#2b2b3a;
  --muted:#7a7a8c;
  --line:#d9dbe6;
  --paper:#ffffff;
  --stage:#e4e5ea;
  --sky1:#8fb3d9;
  --sky2:#2f5d95;
}
*{box-sizing:border-box;margin:0;padding:0}
html,body{width:1200px;height:2448px;overflow:hidden}
body{background:var(--stage);font-family:"Montserrat",Arial,sans-serif;color:var(--ink)}
.sheet{width:1200px;height:2448px;display:flex;flex-direction:column;align-items:center;justify-content:space-evenly;padding:30px 0}
.hero-wrap{width:1080px;height:607px;box-shadow:0 8px 30px rgba(30,30,70,.18)}
.hero-wrap .slide{transform:scale(2.0377);transform-origin:0 0}
.grid{display:grid;grid-template-columns:530px 530px;gap:44px 20px}
.slide{position:relative;width:530px;height:298px;background:var(--paper);overflow:hidden;box-shadow:0 3px 12px rgba(30,30,70,.12)}
.abs{position:absolute}
.photo{position:absolute}
.brandrow{position:absolute;display:flex;gap:10px;align-items:center}
.brand{display:flex;align-items:center;gap:3px;font-weight:700;color:var(--navy);font-size:6.5px;letter-spacing:.3px;line-height:1.1}
.brand i{display:block;width:9px;height:9px;background:var(--navy)}
.bracket{position:absolute;width:14px;height:14px;border-color:var(--navy);border-style:solid}
.bracket.bl{border-width:0 0 3px 3px}
.bracket.tr{border-width:3px 3px 0 0}
.url{position:absolute;font-size:4.5px;color:var(--muted)}
.h-title{font-weight:800;color:var(--navy);font-size:17px;letter-spacing:.3px}
.lead{color:var(--red);font-weight:700;font-size:7px;line-height:1.35}
.body{font-size:4.8px;line-height:1.6;color:var(--muted)}
.band{position:absolute;left:0;top:0;width:100%;height:44px;background:var(--navy);color:#fff;font-weight:800;font-size:15px;padding:14px 28px;letter-spacing:.3px}
.cap{color:var(--red);font-weight:700;font-size:6px;margin:6px 0 3px}
/* cover */
.cover-title{left:28px;top:92px;font-size:22px;line-height:1.05;color:var(--navy);font-weight:500}
.cover-title strong{display:block;font-weight:800;color:var(--red)}
.cover-frame{right:46px;top:66px;width:150px;height:150px;background:var(--navy)}
/* services */
.svc-list{position:absolute;right:26px;top:40px;width:200px;list-style:none}
.svc-list li{font-size:5px;color:var(--ink);padding:4px 8px;border-bottom:1px solid var(--line);display:flex;align-items:center;gap:5px}
.svc-list li::before{content:"";width:4px;height:4px;background:var(--navy)}
.svc-list li.on{background:var(--navy);color:#fff}
.svc-list li.on::before{background:#fff}
/* process */
.step{position:absolute;width:92px;height:52px;border:1px solid var(--line);background:#fff;padding:6px}
.step b{display:block;color:var(--red);font-size:5.5px;margin-bottom:3px}
.step p{font-size:4.2px;line-height:1.5;color:var(--muted)}
/* team */
.member{position:absolute;top:70px;width:100px}
.member .photo{position:relative;width:100px;height:120px}
.tag{background:var(--navy);color:#fff;padding:4px 6px;font-size:5px;font-weight:600}
.tag span{display:block;font-weight:400;font-size:4px;opacity:.8}
/* stats */
.stat{display:flex;gap:8px;align-items:center;margin-top:8px}
.stat b{color:var(--red);font-size:14px;font-weight:800}
/* contact */
.contact{position:absolute;font-size:5px;color:var(--ink);line-height:2.1}
.contact li{list-style:none;display:flex;align-items:center;gap:4px}
</style>
</head>
<body>
<main class="sheet">

  <!-- Title slide shown large -->
  <div class="hero-wrap">
    <section class="slide slide-cover">
      <div class="brandrow" style="left:28px;top:30px">
        <div class="brand"><i></i>BRACKWELL<br>LAW FIRM PC</div>
        <div class="brand"><i></i>BRACKWELL<br>CONSULTING GROUP</div>
      </div>
      <h1 class="abs cover-title">NAVIGATING<br>BORDERS<strong>SECURING<br>FUTURES</strong></h1>
      <div class="abs cover-frame"></div>
      <div class="photo" role="img" aria-label="Business team standing in front of a glowing globe" style="right:66px;top:50px;width:150px;height:150px;background:linear-gradient(160deg,#e8c98a,#6f7fb4 55%,#2d2c73)"></div>
      <div class="bracket bl" style="left:28px;bottom:34px"></div>
      <div class="url" style="left:28px;bottom:18px">www.brackwelllaw.example</div>
    </section>
  </div>

  <div class="grid">
    <!-- 1 Cover -->
    <section class="slide slide-cover">
      <div class="brandrow" style="left:28px;top:30px">
        <div class="brand"><i></i>BRACKWELL<br>LAW FIRM PC</div>
        <div class="brand"><i></i>BRACKWELL<br>CONSULTING GROUP</div>
      </div>
      <h2 class="abs cover-title">NAVIGATING<br>BORDERS<strong>SECURING<br>FUTURES</strong></h2>
      <div class="abs cover-frame"></div>
      <div class="photo" role="img" aria-label="Business team standing in front of a glowing globe" style="right:66px;top:50px;width:150px;height:150px;background:linear-gradient(160deg,#e8c98a,#6f7fb4 55%,#2d2c73)"></div>
      <div class="bracket bl" style="left:28px;bottom:34px"></div>
      <div class="url" style="left:28px;bottom:18px">www.brackwelllaw.example</div>
    </section>

    <!-- 2 About -->
    <section class="slide slide-about">
      <div class="photo" role="img" aria-label="Glass skyscrapers seen from below against a blue sky" style="left:0;top:0;width:230px;height:298px;background:linear-gradient(200deg,var(--sky1),#c9d8ea 40%,var(--sky2))"></div>
      <div class="bracket tr" style="right:26px;top:26px"></div>
      <div class="abs" style="left:256px;top:70px;width:240px">
        <h2 class="h-title">ABOUT US</h2>
        <p class="lead" style="margin:10px 0 8px">A cross-border legal partner for foreign businesses and families entering the United States.</p>
        <p class="body">We guide clients through visas, investment, company formation and compliance with clear advice at every stage. Our team works across languages and time zones so each matter moves forward with care, speed and full transparency.</p>
      </div>
      <div class="brandrow" style="left:256px;bottom:24px">
        <div class="brand"><i></i>BRACKWELL</div>
      </div>
    </section>

    <!-- 3 Services -->
    <section class="slide slide-services">
      <div class="abs" style="left:28px;top:90px;width:190px">
        <h2 class="h-title">OUR SERVICES</h2>
        <p class="lead" style="margin-top:8px">Over 30 years of business success in immigration &amp; corporate law</p>
      </div>
      <ul class="svc-list">
        <li>Business Immigration</li>
        <li>Investor &amp; Entrepreneur Visas</li>
        <li>Family Based Immigration</li>
        <li>Company Formation in the US</li>
        <li class="on">International Business Consulting</li>
        <li>Contracts &amp; Compliance</li>
        <li>Mergers &amp; Acquisitions</li>
        <li>Citizenship &amp; Naturalization</li>
      </ul>
      <div class="brandrow" style="left:28px;bottom:24px">
        <div class="brand"><i></i>BRACKWELL</div>
        <div class="brand"><i></i>BRACKWELL</div>
      </div>
    </section>

    <!-- 4 Process -->
    <section class="slide slide-process">
      <div class="photo" role="img" aria-label="Faint city skyline" style="left:0;top:44px;width:100%;height:70px;background:linear-gradient(180deg,#eef0f6,#ffffff)"></div>
      <div class="band">OUR PROCESS</div>
      <div class="photo" role="img" aria-label="Statue of Lady Justice holding scales" style="right:14px;top:20px;width:70px;height:278px;background:linear-gradient(180deg,#c9b27a,#7a6234 60%,#3e3220)"></div>
      <svg class="abs" style="left:0;top:0" width="530" height="298" aria-hidden="true">
        <g stroke="var(--navy)" stroke-width="1" fill="none">
          <path d="M124 106 H144 M246 106 H266 M124 186 H144 M246 186 H266"/>
          <path d="M78 132 V160 M200 132 V160 M322 132 V160"/>
        </g>
      </svg>
      <div class="step" style="left:32px;top:80px"><b>Consultation</b><p>We review your goals and the options open to you.</p></div>
      <div class="step" style="left:154px;top:80px"><b>Strategy</b><p>A clear plan with timelines and required steps.</p></div>
      <div class="step" style="left:276px;top:80px"><b>Documents</b><p>We prepare and check every filing for accuracy.</p></div>
      <div class="step" style="left:32px;top:160px"><b>Filing</b><p>Applications are submitted and tracked closely.</p></div>
      <div class="step" style="left:154px;top:160px"><b>Follow Up</b><p>We respond to requests and keep you informed.</p></div>
      <div class="step" style="left:276px;top:160px"><b>Approval</b><p>Final guidance as you settle into the US.</p></div>
    </section>

    <!-- 5 Content header -->
    <section class="slide slide-content">
      <h2 class="abs h-title" style="left:28px;top:30px">SLIDE HEADER</h2>
      <div class="brandrow" style="right:28px;top:32px"><div class="brand"><i></i>BRACKWELL</div></div>
      <div class="abs" style="left:28px;top:70px;width:145px">
        <div class="photo" role="img" aria-label="Desk with passports and documents" style="position:relative;width:145px;height:95px;background:linear-gradient(150deg,#a9b8cc,#5a6b86)"></div>
        <p class="cap">Lorem Ipsum</p>
        <p class="body">Short note describing this topic for the audience.</p>
      </div>
      <div class="abs" style="left:192px;top:70px;width:145px">
        <div class="photo" role="img" aria-label="Signing a legal contract" style="position:relative;width:145px;height:95px;background:linear-gradient(150deg,#d7d2c8,#8a8478)"></div>
        <p class="cap">Lorem Ipsum</p>
        <p class="body">Short note describing this topic for the audience.</p>
      </div>
      <div class="abs" style="left:356px;top:70px;width:145px">
        <div class="photo" role="img" aria-label="Business meeting around a table" style="position:relative;width:145px;height:95px;background:linear-gradient(150deg,#c6ccd8,#4c5674)"></div>
        <p class="cap">Lorem Ipsum</p>
        <p class="body">Short note describing this topic for the audience.</p>
      </div>
      <div class="bracket bl" style="left:28px;bottom:20px"></div>
    </section>

    <!-- 6 Team -->
    <section class="slide slide-team">
      <h2 class="abs h-title" style="left:28px;top:30px">OUR TEAM</h2>
      <div class="brandrow" style="right:28px;top:32px"><div class="brand"><i></i>BRACKWELL</div></div>
      <div class="member" style="left:28px"><div class="photo" role="img" aria-label="Portrait of team member" style="background:linear-gradient(180deg,#d9dbe4,#9aa1b6)"></div><div class="tag">Elena Marsh<span>Managing Partner</span></div></div>
      <div class="member" style="left:147px"><div class="photo" role="img" aria-label="Portrait of team member" style="background:linear-gradient(180deg,#d9dbe4,#9aa1b6)"></div><div class="tag">Daniel Ortiz<span>Senior Attorney</span></div></div>
      <div class="member" style="left:266px"><div class="photo" role="img" aria-label="Portrait of team member" style="background:linear-gradient(180deg,#d9dbe4,#9aa1b6)"></div><div class="tag">Sofia Lind<span>Immigration Counsel</span></div></div>
      <div class="member" style="left:385px"><div class="photo" role="img" aria-label="Portrait of team member" style="background:linear-gradient(180deg,#d9dbe4,#9aa1b6)"></div><div class="tag">Martin Hale<span>Business Consultant</span></div></div>
    </section>

    <!-- 7 Title + stats -->
    <section class="slide slide-stats">
      <div class="abs" style="left:28px;top:36px;width:200px">
        <h2 class="h-title">SLIDE TITLE HERE</h2>
        <p class="lead" style="margin:8px 0 6px">Subtitle text goes here</p>
        <p class="body">Add a short supporting statement about results and client trust.</p>
        <div class="stat"><b>61%</b><p class="body">of clients expand to a second US state.</p></div>
        <div class="stat"><b>95%</b><p class="body">approval rate on prepared filings.</p></div>
      </div>
      <div class="photo" role="img" aria-label="Judge's gavel in front of a United States flag" style="right:0;top:0;width:250px;height:298px;background:linear-gradient(120deg,#b23a48,#6e3b2a 45%,#2d2c73)"></div>
      <div class="brandrow" style="left:28px;bottom:22px"><div class="brand"><i></i>BRACKWELL</div></div>
    </section>

    <!-- 8 Contact -->
    <section class="slide slide-contact">
      <div class="band" style="height:52px;text-align:center;padding-top:18px">WE'RE HERE TO HELP!</div>
      <div class="brandrow" style="left:0;right:0;top:86px;justify-content:center;gap:30px">
        <div class="brand" style="font-size:10px"><i style="width:14px;height:14px"></i>BRACKWELL<br>LAW FIRM PC</div>
        <div class="brand" style="font-size:10px"><i style="width:14px;height:14px"></i>BRACKWELL<br>CONSULTING GROUP</div>
      </div>
      <p class="abs lead" style="left:0;right:0;top:150px;text-align:center;font-size:8px">GET IN TOUCH</p>
      <ul class="contact" style="left:110px;top:172px">
        <li><svg width="7" height="7" viewBox="0 0 10 10"><path d="M2 1l2 2-1 1.5c.8 1.5 1.5 2.2 3 3L7.5 6l2 2-1.5 1.5C4 9 1 6 .5 2.5z" fill="var(--navy)"/></svg>(555) 010-2040</li>
        <li><svg width="7" height="7" viewBox="0 0 10 10"><rect x="0.5" y="2" width="9" height="6" fill="none" stroke="var(--navy)"/><path d="M.5 2l4.5 3.5L9.5 2" fill="none" stroke="var(--navy)"/></svg>hello@brackwelllaw.example</li>
      </ul>
      <ul class="contact" style="left:290px;top:172px">
        <li><svg width="7" height="7" viewBox="0 0 10 10"><path d="M5 .5a3.3 3.3 0 0 1 3.3 3.3C8.3 6.5 5 9.5 5 9.5S1.7 6.5 1.7 3.8A3.3 3.3 0 0 1 5 .5z" fill="var(--navy)"/><circle cx="5" cy="3.8" r="1.2" fill="#fff"/></svg>120 Harbor Street, Suite 400</li>
        <li style="padding-left:11px">Riverton, NY 10001</li>
      </ul>
      <div class="bracket bl" style="left:28px;bottom:20px"></div>
    </section>
  </div>
</main>
</body>
</html>
```